**** Business card design for VoltaNode ****

For my ICT company VoltaNode I need I need a business card design.

We design, build and host web-applications and we have our own CMS product.

Some good examples are attached.

The information should be:
Joris Tielenburg
Managing director
E: j.tielenburg@voltanode-example.nl
M: +31(0)6 57218064
T: +31(0)40 7249305
W: www.voltanode-example.nl

Address:
Berend Vlootweg 27
5612 KT Eindhoven

Industry/Entity Type

Business

Requirements
Must have
• - Use logo (see attachments)
- Double sided
- Distinctive
Nice to have
• - Place for a statement on the back-side: "Designed with knowledge, built with passion"
- HTML code (or Wordpress)
- Dark (black or dark-gray) side
- Small simple images for telephone, e-mail en Url.
- QR code (only if not disturbing), not required, just an option

```html
<!DOCTYPE html>
<html lang="en">
<head>
<meta charset="utf-8">
<title>VoltaNode business card</title>
<link rel="stylesheet" href="https://fonts.googleapis.com/css2?family=Tinos:ital,wght@0,400;0,700;1,700&display=swap">
<style>
  :root {
    --backdrop: #7d7d7d;
    --card: #3a3a3c;
    --card-deep: #252527;
    --band: #0b0b0c;
    --cyan: #2fc4f2;
    --cyan-soft: #7fd9f7;
  }
  * { box-sizing: border-box; margin: 0; padding: 0; }
  html, body { width: 1200px; height: 800px; overflow: hidden; }
  body {
    background: radial-gradient(ellipse at 50% 35%, #9a9a9a 0%, var(--backdrop) 55%, #5a5a5a 100%);
    font-family: "Tinos", "Times New Roman", serif;
    position: relative;
  }
  .card {
    position: absolute;
    width: 540px;
    height: 310px;
    overflow: hidden;
    box-shadow: 0 12px 30px rgba(0,0,0,.45);
  }
  .card--front { left: 70px; top: 80px; background: linear-gradient(160deg, #4a4a4d 0%, var(--card) 50%, var(--card-deep) 100%); }
  .card--back { left: 600px; top: 420px; background: linear-gradient(150deg, #47474a 0%, var(--card-deep) 60%, #111 100%); }
  .card__bands { position: absolute; inset: 0; }
  .brand { position: absolute; display: flex; align-items: center; gap: 18px; }
  .brand__dot { border-radius: 50%; background: var(--cyan); }
  .brand__name { color: var(--cyan); font-weight: 700; line-height: 1; }
  .card--front .brand { left: 48px; top: 92px; }
  .card--front .brand__dot { width: 70px; height: 70px; }
  .card--front .brand__name { font-size: 58px; }
  .tagline {
    position: absolute; left: 190px; top: 172px;
    color: var(--cyan); font-weight: 700; font-size: 16px; line-height: 1.25;
  }
  .tagline span { display: block; }
  .tagline span + span { padding-left: 92px; }
  .front-url {
    position: absolute; left: 0; right: 0; top: 252px; text-align: center;
    color: var(--cyan); font-weight: 700; font-size: 22px;
  }
  .card--back .brand { left: 30px; top: 34px; }
  .card--back .brand__dot { width: 62px; height: 62px; }
  .card--back .brand__name { font-size: 48px; }
  .person { position: absolute; left: 250px; top: 106px; color: var(--cyan); font-weight: 700; }
  .person__name { font-size: 26px; line-height: 1.05; }
  .person__role { font-size: 18px; padding-left: 22px; }
  .contact { position: absolute; left: 232px; top: 170px; list-style: none; color: var(--cyan); font-weight: 700; font-size: 13.5px; }
  .contact li { display: flex; align-items: center; gap: 6px; height: 19px; }
  .contact svg { width: 14px; height: 14px; flex: none; }
  .address { position: absolute; left: 252px; top: 250px; color: var(--cyan); font-weight: 700; font-size: 13.5px; line-height: 1.3; }
</style>
</head>
<body>

<section class="card card--front" aria-label="Business card front">
  <svg class="card__bands" viewBox="0 0 540 310" preserveAspectRatio="none" aria-hidden="true">
    <path d="M0 0 H540 V22 C420 10 300 40 160 60 C90 70 40 80 0 95 Z" fill="var(--band)"/>
    <path d="M0 250 C120 270 250 230 380 200 C450 185 500 190 540 200 V310 H0 Z" fill="var(--band)"/>
  </svg>
  <div class="brand">
    <span class="brand__dot"></span>
    <span class="brand__name">VoltaNode</span>
  </div>
  <p class="tagline"><span>“Shaped by insight, always</span><span>Run with steady care”</span></p>
  <p class="front-url">www.voltanode-example.nl</p>
</section>

<section class="card card--back" aria-label="Business card back">
  <svg class="card__bands" viewBox="0 0 540 310" preserveAspectRatio="none" aria-hidden="true">
    <path d="M0 0 H60 C40 100 60 220 120 310 H0 Z" fill="var(--band)" opacity=".8"/>
  </svg>
  <div class="brand">
    <span class="brand__dot"></span>
    <span class="brand__name">VoltaNode</span>
  </div>
  <div class="person">
    <p class="person__name">Joris Tielenburg</p>
    <p class="person__role">Managing director</p>
  </div>
  <ul class="contact">
    <li><svg viewBox="0 0 14 14"><rect x="1" y="3" width="12" height="8" rx="1" fill="none" stroke="var(--cyan-soft)" stroke-width="1.4"/><path d="M1 3 L7 8 L13 3" fill="none" stroke="var(--cyan-soft)" stroke-width="1.4"/></svg>E: j.tielenburg@voltanode-example.nl</li>
    <li><svg viewBox="0 0 14 14"><rect x="4" y="1" width="6" height="12" rx="1.2" fill="none" stroke="var(--cyan-soft)" stroke-width="1.4"/></svg>M: +31(0)6 57218064</li>
    <li><svg viewBox="0 0 14 14"><path d="M2 4 C2 2 4 1 7 1 C10 1 12 2 12 4 L10 5 L9 3.5 H5 L4 5 Z" fill="var(--cyan-soft)"/><rect x="3" y="6" width="8" height="6" rx="1" fill="var(--cyan-soft)"/></svg>T: +31(0)40 7249305</li>
    <li><svg viewBox="0 0 14 14"><circle cx="7" cy="7" r="5.5" fill="var(--cyan)"/></svg>W: www.voltanode-example.nl</li>
  </ul>
  <p class="address">Address:<br>Berend Vlootweg 27<br>5612 KT Eindhoven</p>
</section>

</body>
</html>
```